Brochure Design Project

Using supplied logo and supplied graphics I want a 4-page brochure 81/2x 11" that can be used as a leave behind, a self mailer and a pdf email attachment for promotion purposes.
The cover needs to be visually provocative and support the following questions"
"Have you lost your leadership edge... has your company lost it's momentum... are your employees as engaged as they need to be?"
The inside of the brochure should explain the Harbor Crest Coaching 7 Step process with is explained in the attached PowerPoint.
Back page should be brief bio of me. And Statement about who we work with. I am attaching a tri-fold brochure we designed but do not like because it is bland and the graphic inside is hard to read.
Target Market(s)
"C" level executives (CEO, CIO, CFO, CMO, CRO etc)
Industry/Entity Type
Leadership
Look and feel

```html
<!DOCTYPE html>
<html lang="en">
<head>
<meta charset="utf-8">
<title>Harbor Crest Coaching – Step 5: S.W.O.T. and Block Assessment</title>
<link rel="stylesheet" href="https://fonts.googleapis.com/css2?family=Sorts+Mill+Goudy&display=swap">
<style>
  :root {
    --page-bg: #ffffff;
    --band-blue: #0a6fd6;
    --band-light: #2f93ee;
    --band-edge: #064a9c;
    --ink: #4a4a4a;
    --bullet: #1565c0;
    --goal-bar: #0b7ae0;
    --tile-s: #5fb2ea;
    --tile-w: #e5282a;
    --tile-o: #f3651d;
    --tile-t: #86cf1e;
    --wall-dark: #1d2a6b;
    --wall-light: #7f9bd6;
  }
  * { margin: 0; padding: 0; box-sizing: border-box; }
  html, body { width: 927px; height: 1200px; overflow: hidden; background: var(--page-bg); }
  .page { position: relative; width: 927px; height: 1200px; overflow: hidden; font-family: "Sorts Mill Goudy", Georgia, serif; }

  .title-band {
    position: absolute; left: 0; top: 133px; width: 927px; height: 276px;
    background: linear-gradient(180deg, var(--band-light) 0%, var(--band-blue) 45%, var(--band-blue) 100%);
    border-top: 8px solid var(--band-edge);
    border-bottom: 8px solid var(--band-edge);
  }
  .title-band h1 {
    position: absolute; left: 18px; top: 60px;
    font-weight: 400; font-size: 51px; color: #fff; white-space: nowrap;
  }

  .goal-bar {
    position: absolute; left: 0; top: 504px; width: 426px; height: 61px;
    background: var(--goal-bar);
  }
  .goal-bar h2 {
    position: absolute; left: 61px; top: 8px;
    font-weight: 400; font-size: 40px; color: #fff; letter-spacing: 0.5px;
  }

  .goal-list {
    position: absolute; left: 61px; top: 568px; width: 430px; list-style: none;
  }
  .goal-list li {
    position: relative; font-size: 42px; line-height: 65px; color: var(--ink);
    white-space: nowrap;
  }
  .goal-list li::before {
    content: ""; position: absolute; left: -29px; top: 27px;
    width: 15px; height: 15px; border-radius: 50%; background: var(--bullet);
  }

  .swot-graphic {
    position: absolute; left: 498px; top: 436px; width: 384px; height: 356px;
    background:
      linear-gradient(135deg, var(--tile-s) 0%, var(--tile-w) 40%, var(--tile-o) 65%, var(--tile-t) 100%);
    border: 8px solid #fff;
    box-shadow: 0 2px 6px rgba(0,0,0,0.25);
  }

  .wall-photo {
    position: absolute; left: 503px; top: 821px; width: 377px; height: 282px;
    background: radial-gradient(ellipse at 60% 55%, var(--wall-light) 0%, #3d56a8 40%, var(--wall-dark) 100%);
    box-shadow: 4px 4px 8px rgba(0,0,0,0.3);
  }

  .footer-band {
    position: absolute; left: 0; top: 1118px; width: 927px; height: 82px;
    background: linear-gradient(180deg, var(--band-light) 0%, var(--band-blue) 100%);
    border-top: 8px solid var(--band-edge);
  }
</style>
</head>
<body>
<main class="page">
  <header class="title-band">
    <h1>STEP #5: S.W.O.T. and Block Assessment</h1>
  </header>

  <section class="goal">
    <div class="goal-bar"><h2>GOAL:</h2></div>
    <ul class="goal-list">
      <li>Conduct S.W.O.T and<br>Block Analysis</li>
      <li>Articulate Strengths<br>from customer’s<br>perspective</li>
      <li>Identify internally<br>created obstacles to<br>success.</li>
    </ul>
  </section>

  <div class="swot-graphic" role="img" aria-label="S.W.O.T. graphic with four glossy tiles: blue strengths, red weaknesses, orange opportunities, green threats"></div>

  <div class="wall-photo" role="img" aria-label="Blue brick wall being broken through by a white arrow"></div>

  <footer class="footer-band"></footer>
</main>
</body>
</html>
```